Infographic Illustration Design Project

We need an infographic fo a foundation based in Vancouver, BC, Canada.
We need it to be bold and colourful and show what we've done as a foundation over the last year.
Here is the content needed to put into the infographic:
BRIGHT HARBOR FOUNDATION
INFOGRAPHIC
www.brightharbor-example.org
Top section
Image: Map of the world
Text: Where Bright Harbor Foundation is Investing
(see image here for where to pins on the map of the world) http://www.brightharbor-example.org/about/about.aspx?page=2
Next section
What is the Bright Harbor Foundation Providing for Missionaries?
Image: Video camera
Text in video camera image: 82
82 Video Cameras Shipquicked Overseas
Image: Web Page
Text in web page: 116
116 Web Pages Created
Image: Dollar Bill
Text in Dollar Bill: $6,000
$6,000 in Matching Funds
Image: E-Mail
Text in E-Mail: 67
67 Fundraising Training E-Letters Sent
Missionaries Telling their Story
Image: Vidstream Video
Text: 110
110 Videos Uploaded from the Field
Image: Cell phone
Text 214
214 Text Messages Sent from the Field
Image: Poloroid photo
Text: 580
580 Photos Uploaded from the Field
Funds were raised
In MASSIVE text: $331,291.55
smaller text: Raised for Missionaries and Wired Overseas
Through various ways
Image: beer glass
Text: 1
1 Champion Who Gave Up Beer to Raise Money for Missions
Image: Wedding Cake Topper
Text: 1
1 Champion Who Gave Up their Wedding to Raise Money for Missions
Image: Birthday Present
Text: 1
1 Champion who Gave up Their Birthday to Raise Money for Missions
Image: People
Text 83
83 People Who Have Fundraised for a Missionary
*Stats are up to date as of Nov, 2012
Our website: www.brightharbor-example.org
Target Market(s)
18-60 year olds who have given to the foundation
Industry/Entity Type
Camera

```html
<!DOCTYPE html>
<html lang="en">
<head>
<meta charset="utf-8">
<title>Bright Harbor Foundation — Year in Review</title>
<link href="https://fonts.googleapis.com/css2?family=Quicksand:wght@400;500;600&display=swap" rel="stylesheet">
<style>
  :root {
    --red-band: #ec7b6e;
    --red-ribbon: #e0544f;
    --red-fold: #b83d39;
    --light: #f1f1f1;
    --gray-ribbon: #dcdcdc;
    --gray-fold: #a9a9a9;
    --yellow-band: #f5e461;
    --amber: #f6b733;
    --amber-fold: #d9931a;
    --blue-band: #9fd1f0;
    --blue: #4fb0df;
    --blue-fold: #2f88b8;
    --ink: #555555;
    --footer: #575757;
    --white: #ffffff;
  }
  * { box-sizing: border-box; margin: 0; padding: 0; }
  html, body { width: 1187px; height: 1200px; overflow: hidden; }
  body { font-family: "Quicksand", sans-serif; background: var(--white); position: relative; color: var(--ink); }

  .band { position: absolute; left: 0; width: 1187px; }
  .band--provided { top: 0; height: 90px; background: var(--red-band); }
  .band--story-title { top: 90px; height: 126px; background: var(--light); }
  .band--story { top: 222px; height: 344px; background: var(--yellow-band); }
  .band--funds { top: 566px; height: 166px; background: var(--white); }
  .band--ways { top: 738px; height: 352px; background: var(--blue-band); }
  .band--footer { top: 1090px; height: 110px; background: var(--footer); }

  .ribbon {
    position: absolute; transform: translateX(-50%);
    color: var(--white); font-size: 13px; line-height: 16px; text-align: center;
    display: flex; align-items: center; justify-content: center; white-space: nowrap;
  }
  .ribbon::before, .ribbon::after {
    content: ""; position: absolute; top: 8px; bottom: -8px; width: 34px; z-index: -1;
  }
  .ribbon::before { left: -22px; clip-path: polygon(0 0, 100% 0, 100% 100%, 0 100%, 40% 50%); }
  .ribbon::after { right: -22px; clip-path: polygon(0 0, 100% 0, 60% 50%, 100% 100%, 0 100%); }
  .ribbon--red { background: var(--red-ribbon); }
  .ribbon--red::before, .ribbon--red::after { background: var(--red-fold); }
  .ribbon--amber { background: var(--amber); }
  .ribbon--amber::before, .ribbon--amber::after { background: var(--amber-fold); }
  .ribbon--blue { background: var(--blue); }
  .ribbon--blue::before, .ribbon--blue::after { background: var(--blue-fold); }

  .top-icon { position: absolute; top: 0; height: 20px; transform: translateX(-50%); background: var(--white); border-radius: 0 0 8px 8px; }

  .title-ribbon {
    position: absolute; left: 50%; transform: translateX(-50%);
    background: var(--gray-ribbon); font-size: 30px; line-height: 40px; font-weight: 500; color: var(--ink);
    display: flex; align-items: flex-start; justify-content: center; letter-spacing: 0.5px;
  }
  .title-ribbon::before, .title-ribbon::after {
    content: ""; position: absolute; top: 20px; bottom: -14px; width: 80px; background: var(--gray-fold); z-index: -1;
  }
  .title-ribbon::before { left: -60px; clip-path: polygon(0 0, 100% 0, 100% 100%, 0 100%, 40% 50%); }
  .title-ribbon::after { right: -60px; clip-path: polygon(0 0, 100% 0, 60% 50%, 100% 100%, 0 100%); }
  .title-ribbon .rule {
    position: absolute; left: 18px; right: 18px; bottom: 10px; height: 2px; background: var(--ink);
  }
  .title-ribbon .rule::after {
    content: ""; position: absolute; left: 50%; top: -3px; width: 8px; height: 8px; margin-left: -4px; border-radius: 50%; background: var(--ink);
  }
  .title-ribbon--story { top: 112px; width: 708px; height: 62px; padding-top: 6px; }
  .title-ribbon--funds { top: 586px; width: 470px; height: 58px; padding-top: 4px; }

  .stat { position: absolute; transform: translateX(-50%); }
  .badge {
    position: absolute; left: 50%; transform: translateX(-50%);
    border-radius: 50%; color: var(--white); font-size: 25px; font-weight: 500;
    display: flex; align-items: center; justify-content: center;
  }
  .badge--amber { background: var(--amber); width: 60px; height: 60px; }
  .badge--blue { background: var(--blue); width: 60px; height: 60px; }
  .disc { position: absolute; left: 50%; transform: translateX(-50%); border-radius: 50%; background: var(--white); display: flex; align-items: center; justify-content: center; }
  .disc--amber { width: 204px; height: 204px; box-shadow: 0 0 0 6px var(--amber); }
  .disc--blue { width: 180px; height: 180px; box-shadow: 0 0 0 4px #d4ecfa; }
  .art { border-radius: 10px; }

  .funds-total { position: absolute; top: 644px; left: 0; width: 1187px; text-align: center; font-size: 46px; line-height: 46px; font-weight: 500; color: var(--ink); letter-spacing: 1px; }
  .funds-sub { position: absolute; top: 697px; left: 0; width: 1187px; text-align: center; font-size: 22px; line-height: 24px; color: var(--ink); letter-spacing: 0.6px; }

  .footer-name { position: absolute; top: 1108px; left: 0; width: 1187px; text-align: center; font-size: 39px; line-height: 46px; color: var(--white); letter-spacing: 1px; }
  .footer-url { position: absolute; top: 1156px; left: 0; width: 1187px; text-align: center; font-size: 27px; line-height: 34px; color: var(--white); }
  .footer-url span { display: inline-block; width: 140px; height: 2px; background: var(--white); vertical-align: middle; margin: 0 12px; }
</style>
</head>
<body>
  <section class="band band--provided">
    <div class="top-icon" style="left:168px;width:100px;"></div>
    <div class="top-icon" style="left:462px;width:110px;"></div>
    <div class="top-icon" style="left:738px;width:120px;background:#7a9a6c;"></div>
    <div class="top-icon" style="left:1034px;width:110px;"></div>
    <div class="ribbon ribbon--red" style="left:168px;top:22px;width:200px;height:40px;">82 video cameras<br>shipquicked overseas</div>
    <div class="ribbon ribbon--red" style="left:462px;top:22px;width:200px;height:32px;">116 webpages created</div>
    <div class="ribbon ribbon--red" style="left:738px;top:22px;width:200px;height:32px;">$6000 in matching funds</div>
    <div class="ribbon ribbon--red" style="left:1034px;top:22px;width:200px;height:40px;">67 fundraising training<br>e-letters sent</div>
  </section>

  <section class="band band--story-title"></section>
  <h2 class="title-ribbon title-ribbon--story">Missionaries telling their story<i class="rule"></i></h2>

  <section class="band band--story"></section>
  <div class="stat" style="left:256px;top:236px;">
    <div class="badge badge--amber" style="top:0;">580</div>
    <div class="disc disc--amber" style="top:84px;">
      <div class="art" role="img" aria-label="Stack of instant photos" style="width:150px;height:110px;background:linear-gradient(135deg,#5a5a5a,#3e3e3e);"></div>
    </div>
  </div>
  <div class="ribbon ribbon--amber" style="left:256px;top:490px;width:224px;height:40px;">580 photos uploaded<br>from the field</div>

  <div class="stat" style="left:576px;top:236px;">
    <div class="badge badge--amber" style="top:0;">110</div>
    <div class="disc disc--amber" style="top:84px;">
      <div class="art" role="img" aria-label="Film strip with play button" style="width:120px;height:150px;background:linear-gradient(#4a4a4a,#3a3a3a);"></div>
    </div>
  </div>
  <div class="ribbon ribbon--amber" style="left:576px;top:490px;width:224px;height:40px;">110 videos uploaded<br>from the field</div>

  <div class="stat" style="left:932px;top:236px;">
    <div class="badge badge--amber" style="top:0;">214</div>
    <div class="disc disc--amber" style="top:84px;">
      <svg width="90" height="160" viewBox="0 0 90 160" aria-label="Mobile phone" role="img">
        <rect x="5" y="20" width="80" height="140" rx="14" fill="#4a4a4a"/>
        <rect x="14" y="38" width="62" height="92" fill="#ffffff"/>
        <circle cx="45" cy="145" r="6" fill="#ffffff"/>
        <rect x="63" y="0" width="4" height="22" fill="#4a4a4a"/>
      </svg>
    </div>
  </div>
  <div class="ribbon ribbon--amber" style="left:932px;top:490px;width:224px;height:40px;">214 text messages sent<br>from the field</div>

  <section class="band band--funds"></section>
  <h2 class="title-ribbon title-ribbon--funds">Funds were raised<i class="rule"></i></h2>
  <p class="funds-total">$331,291.55</p>
  <p class="funds-sub">raised for 32 missionaries through various ways</p>

  <section class="band band--ways"></section>
  <div class="stat" style="left:166px;top:764px;">
    <div class="badge badge--blue" style="top:0;">1</div>
    <div class="disc disc--blue" style="top:66px;">
      <div class="art" role="img" aria-label="Glass of beer" style="width:76px;height:140px;background:linear-gradient(#ffffff 0 14%,#f8c627 14%);"></div>
    </div>
  </div>
  <div class="ribbon ribbon--blue" style="left:166px;top:986px;width:206px;height:40px;">1 champion gave up beer<br>to raise money for missions</div>

  <div class="stat" style="left:445px;top:764px;">
    <div class="badge badge--blue" style="top:0;">2</div>
    <div class="disc disc--blue" style="top:66px;">
      <div class="art" role="img" aria-label="Wedding couple, groom and bride" style="width:150px;height:140px;background:linear-gradient(90deg,#2f2f2f 0 50%,#f4f4f4 50%);"></div>
    </div>
  </div>
  <div class="ribbon ribbon--blue" style="left:445px;top:986px;width:206px;height:54px;">2 champions gave up their<br>wedding to raise money<br>for missions</div>

  <div class="stat" style="left:737px;top:764px;">
    <div class="badge badge--blue" style="top:0;">1</div>
    <div class="disc disc--blue" style="top:66px;">
      <div class="art" role="img" aria-label="Wrapped birthday present" style="width:130px;height:120px;background:linear-gradient(90deg,#c596cf 0 44%,#ef4c8a 44% 56%,#c596cf 56%);"></div>
    </div>
  </div>
  <div class="ribbon ribbon--blue" style="left:737px;top:986px;width:206px;height:54px;">1 champion gave up their<br>birthday to raise money<br>for missions</div>

  <div class="stat" style="left:1026px;top:764px;">
    <div class="badge badge--blue" style="top:0;">83</div>
    <div class="disc disc--blue" style="top:66px;">
      <div class="art" role="img" aria-label="Money bag with dollar sign" style="width:110px;height:130px;border-radius:40px 40px 30px 30px;background:#8b6b47;"></div>
    </div>
  </div>
  <div class="ribbon ribbon--blue" style="left:1026px;top:986px;width:206px;height:40px;">83 people have created<br>fundraising pages</div>

  <footer class="band band--footer"></footer>
  <p class="footer-name">Bright Harbor Foundation</p>
  <p class="footer-url"><span></span>www.brightharbor-example.org<span></span></p>
</body>
</html>
```